8 Page Publishing/Entertainment Website Design

We need a slick, polished, professional looking fully mobile responsive website designed for the publishing / entertainment industry. It will contain 8 pages, including the Home page. The site is to be designed in pure HTML and CSS only and to be compatible with any type of server we put it on. Pages are *not* to be part of any template system, like WordPress or others like it. Pure HTML and CSS standalone pages only. No WordPress or Joomla, etc. Website to use our logo's colors of red/white throughout its design. Uploaded files contain a word DOC that outlines more of our needs and we have included our logo file. Please read the specifications in the Word Document attached. We have also included a PDF file with the website specs as well.

Target Market(s)

Authors and Screenwriters

Coding

Coded - Design and coding required

Number of Pages Required

5+ page

Colors
ec1f27
ffffff
f04a50
f59195

Requirements
Must have
• The site is to be designed in pure HTML and CSS only and to be compatible with any type of server we put it on. Pages are *not* to be part of any template system, like WordPress or others like it. Pure HTML and CSS standalone pages only. No WordPress or Joomla, etc. Website to use our logo's colors of red/white throughout its design. Uploaded files contain a word DOC that outlines more of our needs and we have included our logo file. Please read the specifications in the Word Document attached. We have also included a PDF file with the website specs as well.
Should not have
• No Wordpress or other Template type pages. Pure HTML and CSS only. Some Javascript and JQuery is okay, upon approval.

```html
<!DOCTYPE html>
<html lang="en">
<head>
<meta charset="utf-8">
<title>Northline Press</title>
<link href="https://fonts.googleapis.com/css2?family=Roboto:ital,wght@0,400;0,500;0,700;0,900;1,400&display=swap" rel="stylesheet">
<style>
:root{
  --red:#ec1f27;
  --red-soft:#f04a50;
  --pink:#f59195;
  --white:#ffffff;
  --ink:#222222;
  --text:#555555;
  --muted:#8a8a8a;
  --line:#dddddd;
  --light:#efefef;
  --dark:#2b2b2b;
  --darker:#1f1f1f;
  --gold:#e3b23c;
}
*{box-sizing:border-box;margin:0;padding:0}
html,body{width:1200px;height:4545px;overflow:hidden}
body{font-family:'Roboto',Arial,sans-serif;color:var(--text);background:var(--white);font-size:12px;line-height:1.5}
.wrap{width:856px;margin:0 auto;position:relative}
section,header,footer{position:relative;width:1200px;overflow:hidden}
.ph{display:block}
.btn-outline{display:inline-block;border:1px solid var(--ink);color:var(--ink);font-size:10px;font-weight:700;padding:6px 12px;text-transform:uppercase;letter-spacing:.5px}
.btn-outline.red{border-color:var(--red);color:var(--red)}
.date{font-size:9px;color:var(--muted)}
.date::before{content:"";display:inline-block;width:7px;height:7px;border:1px solid currentColor;border-radius:50%;margin-right:4px;vertical-align:-1px}
.sec-title{font-size:16px;font-weight:700;color:var(--ink);text-transform:uppercase;padding-bottom:6px;position:relative;display:inline-block}
.sec-title::after{content:"";position:absolute;left:0;bottom:0;width:40px;height:3px;background:var(--red)}

/* header */
.site-header{height:115px;background:var(--white);border-top:4px solid var(--dark)}
.site-header .wrap{display:flex;align-items:center;justify-content:space-between;height:111px}
.nav{display:flex;gap:22px;font-size:12px;font-weight:500;color:var(--ink);text-transform:uppercase;width:320px}
.nav.right{justify-content:flex-end}
.brand{display:flex;align-items:center;gap:8px;color:var(--red);font-weight:900;font-size:17px;text-transform:uppercase;letter-spacing:.5px}
.brand i{width:26px;height:26px;border-radius:50%;background:var(--red);display:block}

/* hero */
.hero{height:505px;background:linear-gradient(135deg,#d8141c,var(--red) 50%,#c9121a)}
.hero-video{position:absolute;left:297px;top:43px;width:612px;height:363px;border:6px solid var(--white);background:linear-gradient(120deg,#3a3a3a,#6b5a4d 45%,#2a2a2a);box-shadow:0 6px 18px rgba(0,0,0,.3)}
.play{position:absolute;left:50%;top:50%;transform:translate(-50%,-50%)}
.hero-btn{position:absolute;left:525px;top:448px;width:150px;height:40px;background:var(--white);color:var(--ink);font-weight:700;font-size:14px;display:flex;align-items:center;justify-content:center;gap:8px;text-transform:uppercase}

/* news */
.news{height:290px;background:var(--light);padding-top:35px}
.news-grid{display:grid;grid-template-columns:repeat(4,1fr);gap:12px;margin-top:18px}
.news-card .ph{height:135px}
.news-card .date{margin-top:8px;display:block}
.news-card h3{font-size:11px;font-weight:700;color:var(--ink);line-height:1.4;margin-top:2px}

/* ad + popular */
.feature{height:678px;padding-top:53px}
.ad{height:146px;display:flex;background:linear-gradient(90deg,#2f2f2f 0,#3a3a3a 50%,#cfcfcf 50%,#dcdcdc 100%);align-items:center;position:relative}
.ad-left{width:50%;padding-left:45px;color:var(--white)}
.ad-left small{font-size:12px;display:block}
.ad-left strong{font-size:20px;font-weight:700}
.ad-mark{position:absolute;left:50%;top:50%;transform:translate(-50%,-50%);width:96px;height:96px;border-radius:50%;background:var(--red);border:5px solid var(--white)}
.ad-right{width:50%;padding-left:90px;font-size:20px;font-weight:700;color:#a8a8a8}
.popular{display:grid;grid-template-columns:197px 418px 200px;gap:21px;margin-top:27px}
.col-title{font-size:13px;font-weight:700;color:var(--ink);margin-bottom:8px}
.pop-left .ph{height:120px}
.pop-list li{list-style:none;display:flex;gap:8px;align-items:flex-start;border-bottom:1px solid var(--line);padding:10px 0}
.pop-list b{font-size:40px;line-height:1;color:#e4e4e4;font-weight:900;width:26px}
.pop-list p{font-size:10px;color:var(--ink);line-height:1.35}
.pop-list span{font-size:8px;color:var(--muted);display:block}
.pop-main .ph{height:267px}
.pop-main .date{display:block;margin-top:10px}
.pop-main h2{font-size:17px;font-weight:700;color:var(--ink);margin:2px 0 6px}
.pop-main p{font-size:10px;line-height:1.5}
.pop-main .foot{display:flex;justify-content:space-between;align-items:center;margin-top:12px}
.stats{font-size:9px;color:var(--muted)}
.tabs{display:flex;gap:14px;font-size:11px;font-weight:700;color:var(--ink);border-bottom:1px solid var(--line);padding-bottom:6px;margin-bottom:8px}
.tabs span:first-child{color:var(--red)}
.side-item{display:flex;gap:8px;padding:7px 0;border-bottom:1px solid #eee}
.side-item .ph{width:62px;height:44px;flex:none}
.side-item p{font-size:9px;line-height:1.35;color:var(--text)}

/* entertainment */
.ent{height:388px;background:var(--dark);padding-top:39px}
.ent-label{position:absolute;left:128px;top:345px;transform:rotate(-90deg);transform-origin:left top;font-size:40px;line-height:1;font-weight:900;color:rgba(255,255,255,.08);white-space:nowrap}
.ent-grid{display:grid;grid-template-columns:418px 206px 215px;gap:8px;height:306px;position:relative}
.ent-card{position:relative}
.ent-card .ph{height:306px}
.ent-card .cap{position:absolute;left:18px;bottom:18px;color:var(--white)}
.ent-card .cap .date{color:var(--white)}
.ent-card h3{font-size:15px;font-weight:700;line-height:1.2}
.ent-card .play{top:44%}

/* categories */
.cats{height:403px;background:var(--pink);padding-top:45px}
.cats .wrap{display:flex;gap:34px}
.cats .frame{width:433px;height:318px;background:var(--white);padding:8px;flex:none}
.cats .frame .ph{height:100%}
.copy h2{font-size:22px;font-weight:700;color:var(--ink);line-height:1.25;margin:10px 0 12px}
.copy p{font-size:10.5px;color:#3d3d3d;margin-bottom:10px;line-height:1.55}

/* authors sales */
.sales{height:394px;padding-top:45px}
.sales .wrap{display:flex;gap:34px}
.sales .copy{width:390px}
.sales .copy p{color:var(--text)}
.sales .frame{width:424px;height:309px;border:1px solid var(--line);padding:6px;flex:none}
.sales .frame .ph{height:100%}

/* newsletter */
.newsletter{height:221px;background:var(--red);text-align:center;color:var(--white);padding-top:48px}
.newsletter h2{font-size:24px;font-weight:700;text-transform:uppercase}
.newsletter p{font-size:14px;margin-top:10px}
.nl-form{display:flex;gap:10px;margin-top:24px}
.field{background:var(--white);height:32px;flex:1;display:flex;align-items:center;padding-left:12px;color:#999;font-size:10px;text-align:left}
.nl-form .submit{width:120px;background:var(--ink);color:var(--white);font-size:10px;font-weight:700;display:flex;align-items:center;justify-content:center}

/* about authors */
.authors{height:370px;text-align:center;padding-top:45px}
.authors h2{font-size:26px;font-weight:700;color:var(--ink)}
.dots{display:flex;justify-content:center;gap:6px;margin-top:8px}
.dots i{width:7px;height:7px;border-radius:50%;background:var(--ink);display:block}
.dots i:nth-child(2){background:var(--red)}
.author-grid{display:grid;grid-template-columns:1fr 1fr;gap:40px;margin-top:30px;text-align:left}
.author{display:flex;gap:18px}
.author .ph{width:150px;height:165px;flex:none}
.author h3{font-size:12px;font-weight:700;color:var(--ink);text-transform:uppercase}
.author small{font-size:9px;color:var(--muted)}
.author p{font-size:10px;margin:6px 0 8px;line-height:1.5}
.socials{display:flex;gap:6px;margin-bottom:10px}
.socials i{width:18px;height:18px;border:1px solid var(--line);border-radius:50%;display:block}

/* testimonials */
.testimonials{height:318px;background:repeating-linear-gradient(45deg,#ececec 0 2px,#e4e4e4 2px 4px);text-align:center;padding-top:38px}
.testimonials h2{font-size:28px;font-weight:900;color:var(--ink);text-transform:uppercase}
.avatar{width:92px;height:92px;border-radius:50%;background:linear-gradient(135deg,#b9b9b9,#8f8f8f);border:4px solid var(--white);margin:12px auto 14px}
.testimonials blockquote{width:960px;margin:0 auto;font-size:12px;font-style:italic;color:var(--text);line-height:1.6}
.who{margin-top:12px;font-size:12px;color:var(--ink)}
.who::before,.who::after{content:"";display:inline-block;width:50px;height:1px;background:var(--ink);vertical-align:middle;margin:0 10px}
.arrow{position:absolute;top:190px;width:30px;height:30px;border-radius:50%;background:var(--white);border:1px solid var(--line);display:flex;align-items:center;justify-content:center}
.arrow.l{left:82px}.arrow.r{right:82px}

/* guarantee */
.guarantee{height:433px;text-align:center;padding-top:40px}
.badge{display:block;width:150px;height:150px;border-radius:50%;background:var(--red);margin:0 auto 10px}
.guarantee h3{font-size:22px;font-weight:700;color:var(--ink);margin-top:14px;text-transform:uppercase}
.guarantee h2{font-size:44px;font-weight:900;color:var(--ink);line-height:1.1;text-transform:uppercase}
.guarantee p{font-size:20px;color:var(--ink);text-transform:uppercase}
.cta{display:inline-block;background:var(--red);color:var(--white);font-size:18px;font-weight:700;padding:10px 30px;margin-top:16px;text-transform:uppercase}

/* footer */
.site-footer{height:358px;background:var(--dark);color:#cfcfcf;padding-top:50px}
.foot-grid{display:grid;grid-template-columns:270px 300px 1fr;gap:28px}
.site-footer h4{font-size:14px;font-weight:700;color:var(--white);text-transform:uppercase;margin-bottom:16px}
.contact-item{display:flex;gap:8px;margin-bottom:10px;font-size:11px}
.contact-item svg{flex:none;margin-top:2px}
.contact-item b{display:block;color:var(--white);font-size:11px;text-transform:uppercase}
.insta{display:grid;grid-template-columns:repeat(4,48px);gap:6px}
.insta i{display:block;height:48px}
.ff{height:32px;border:1px solid #555;margin-bottom:10px;color:#888;font-size:10px;padding:8px 10px}
.ff.msg{height:80px}
.send{display:inline-block;background:var(--red);color:var(--white);font-weight:700;font-size:12px;padding:7px 18px;text-transform:uppercase}
.bottom-bar{height:72px;background:var(--red);color:var(--white);text-align:center;padding-top:16px;font-size:11px}
.bottom-bar nav{text-transform:uppercase;font-weight:500;word-spacing:4px}
.bottom-bar small{display:block;font-size:9px;margin-top:4px;opacity:.9}
</style>
</head>
<body>

<header class="site-header">
  <div class="wrap">
    <nav class="nav"><span>Home</span><span>About NLP</span><span>Apply Now</span><span>NLP Worlds</span></nav>
    <div class="brand"><i></i>Northline Press</div>
    <nav class="nav right"><span>NLP Authors</span><span>FAQ</span><span>News</span><span>Contact Us</span></nav>
  </div>
</header>

<section class="hero">
  <div class="hero-video ph" role="img" aria-label="Featured video still of two smiling celebrities at a premiere">
    <svg class="play" width="70" height="70" viewBox="0 0 70 70"><circle cx="35" cy="35" r="33" fill="#ec1f27"/><path d="M28 22 L50 35 L28 48 Z" fill="#fff"/></svg>
  </div>
  <div class="hero-btn"><svg width="14" height="14" viewBox="0 0 14 14"><rect x="1" y="3" width="10" height="10" fill="none" stroke="#222" stroke-width="1.5"/><path d="M5 9 L12 2" stroke="#222" stroke-width="1.5"/></svg>Apply Now</div>
</section>

<section class="news">
  <div class="wrap">
    <h2 class="sec-title">News &amp; Trending</h2>
    <div class="news-grid">
      <article class="news-card"><div class="ph" role="img" aria-label="Photo of guests posing at a gala event" style="background:linear-gradient(135deg,#5a4a44,#a08a7a)"></div><span class="date">March 13, 2018</span><h3>Lorem Ipsum is simply dummy text the printing and typesetting industry.</h3></article>
      <article class="news-card"><div class="ph" role="img" aria-label="Photo of a presenter on a television stage" style="background:linear-gradient(135deg,#2e3a5a,#c0705a)"></div><span class="date">March 13, 2018</span><h3>Lorem Ipsum is simply dummy text the printing and typesetting industry.</h3></article>
      <article class="news-card"><div class="ph" role="img" aria-label="Photo of a celebrity couple on a red carpet" style="background:linear-gradient(135deg,#3a2a2a,#8a6a5a)"></div><span class="date">March 13, 2018</span><h3>Lorem Ipsum is simply dummy text the printing and typesetting industry.</h3></article>
      <article class="news-card"><div class="ph" role="img" aria-label="Photo of a concert crowd under stage lights" style="background:linear-gradient(135deg,#3a1e14,#d28a4a)"></div><span class="date">March 13, 2018</span><h3>Lorem Ipsum is simply dummy text the printing and typesetting industry.</h3></article>
    </div>
  </div>
</section>

<section class="feature">
  <div class="wrap">
    <div class="ad">
      <div class="ad-left"><small>This is an Advertisement</small><strong>The Justice is at Hands</strong></div>
      <div class="ad-mark"></div>
      <div class="ad-right">Your Ad Space Here</div>
    </div>
    <div class="popular">
      <div class="pop-left">
        <div class="col-title">Most Popular</div>
        <div class="ph" role="img" aria-label="Photo of two actors at a press event" style="background:linear-gradient(135deg,#3a3030,#8a7060)"></div>
        <ul class="pop-list">
          <li><b>1</b><p>Meet the Top Models of Fall 2018<span>27 Shares</span></p></li>
          <li><b>2</b><p>Residents Seem to Have Found the Key to Happiness<span>27 Shares</span></p></li>
          <li><b>3</b><p>Grandfather Comes Home to a Warm Surprise<span>27 Shares</span></p></li>
        </ul>
      </div>
      <div class="pop-main">
        <div class="ph" role="img" aria-label="Photo of a group of women in evening dresses at an awards night" style="background:linear-gradient(135deg,#2a2020,#7a5a4a 50%,#3a2a2a)"></div>
        <span class="date">March 13, 2018</span>
        <h2>Reality Check: Counting the Cost of Brexit</h2>
        <p>Lorem Ipsum has been the industry's standard dummy text ever since the 1500s, when an unknown printer took a galley of type and scrambled it to make a type specimen book. Lorem Ipsum has been the industry's standard dummy text ever since the 1500s, when an unknown printer took a galley of type and scrambled it to make a type specimen book.</p>
        <div class="foot"><span class="btn-outline red">Continue Reading</span><span class="stats">♡ 09 &nbsp; ◯ 23 &nbsp; ◎ 12</span></div>
      </div>
      <div class="pop-side">
        <div class="tabs"><span>Latest</span><span>Popular</span><span>Comments</span></div>
        <div class="side-item"><div class="ph" role="img" aria-label="Thumbnail of a celebrity portrait" style="background:#8a6a5a"></div><div><span class="date">March 13, 2018</span><p>Industry's standard unknown printer took</p></div></div>
        <div class="side-item"><div class="ph" role="img" aria-label="Thumbnail of a stage performance" style="background:#6a3a7a"></div><div><span class="date">March 13, 2018</span><p>Industry's standard unknown printer took</p></div></div>
        <div class="side-item"><div class="ph" role="img" aria-label="Thumbnail of a concert light show" style="background:#7a2a6a"></div><div><span class="date">March 13, 2018</span><p>Industry's standard unknown printer took</p></div></div>
        <div class="side-item"><div class="ph" role="img" aria-label="Thumbnail of a fashion event" style="background:#5a4a5a"></div><div><span class="date">March 13, 2018</span><p>Industry's standard unknown printer took</p></div></div>
        <div class="side-item"><div class="ph" role="img" aria-label="Thumbnail of an actress portrait" style="background:#9a7a6a"></div><div><span class="date">March 13, 2018</span><p>Industry's standard unknown printer took</p></div></div>
      </div>
    </div>
  </div>
</section>

<section class="ent">
  <div class="ent-label">Entertainment</div>
  <div class="wrap">
    <div class="ent-grid">
      <article class="ent-card"><div class="ph" role="img" aria-label="Photo of a singer performing on stage with a microphone" style="background:linear-gradient(135deg,#e0602a,#b8281e 60%,#6a1414)"></div><div class="cap"><span class="date">March 13, 2018</span><h3>Lorem Ipsum is simply the printing<br>and typesetting.</h3></div></article>
      <article class="ent-card"><div class="ph" role="img" aria-label="Video still of a nightclub dance floor" style="background:linear-gradient(160deg,#3a1a6a,#c03a8a 60%,#4a1a5a)"></div><svg class="play" width="44" height="44" viewBox="0 0 44 44"><circle cx="22" cy="22" r="20" fill="none" stroke="#fff" stroke-width="2"/><path d="M18 14 L31 22 L18 30 Z" fill="#fff"/></svg><div class="cap"><span class="date">March 13, 2018</span><h3>Lorem Ipsum is simply<br>the printing and typesetting.</h3></div></article>
      <article class="ent-card"><div class="ph" role="img" aria-label="Video still of a concert with purple stage lights" style="background:linear-gradient(160deg,#1a1040,#7a2aa0 55%,#2a1040)"></div><svg class="play" width="44" height="44" viewBox="0 0 44 44"><circle cx="22" cy="22" r="20" fill="none" stroke="#fff" stroke-width="2"/><path d="M18 14 L31 22 L18 30 Z" fill="#fff"/></svg><div class="cap"><span class="date">March 13, 2018</span><h3>Lorem Ipsum is simply<br>the printing and typesetting.</h3></div></article>
    </div>
  </div>
</section>

<section class="cats">
  <div class="wrap">
    <div class="frame"><div class="ph" role="img" aria-label="Collage of fashion magazine covers" style="background:linear-gradient(135deg,#e8c84a,#e04a6a 50%,#5aa0d0)"></div></div>
    <div class="copy">
      <h2>Discover Bestselling Book Categories<br>in Seconds</h2>
      <p>Lorem Ipsum has been the industry's standard dummy text ever since the 1500s, when an unknown printer took a galley of type and scrambled it to make a type specimen book. It has survived not only five centuries, but also the leap into electronic typesetting, remaining essentially unchanged. It was popularised in the 1960s with the release of Letraset sheets containing Lorem Ipsum passages.</p>
      <p>Lorem Ipsum has been the industry's standard dummy text ever since the 1500s, when an unknown printer took a galley of type and scrambled it to make a type specimen book. It was popularised in the 1960s with the release of Letraset sheets, and more recently with desktop publishing software.</p>
      <span class="btn-outline">Read More ›</span>
    </div>
  </div>
</section>

<section class="sales">
  <div class="wrap">
    <div class="copy">
      <h2>Learn About Other Authors &amp; Their Sales</h2>
      <p>Lorem Ipsum has been the industry's standard dummy text ever since the 1500s, when an unknown printer took a galley of type and scrambled it to make a type specimen book. It has survived not only five centuries, but also the leap into electronic typesetting, remaining essentially unchanged. It was popularised in the 1960s with the release of Letraset sheets containing Lorem Ipsum passages, and more recently with desktop publishing software.</p>
      <p>Lorem Ipsum has been the industry's standard dummy text ever since the 1500s, when an unknown printer took a galley of type and scrambled it to make a type specimen book. It has survived not only five centuries, but also the leap into electronic typesetting, remaining essentially unchanged.</p>
      <span class="btn-outline">Read More ›</span>
    </div>
    <div class="frame"><div class="ph" role="img" aria-label="Photo of a speaker at a podium during a charity gala" style="background:linear-gradient(135deg,#1a1a1a,#5a5a5a 50%,#2a2a2a)"></div></div>
  </div>
</section>

<section class="newsletter">
  <div class="wrap">
    <h2>Sign Up for Newsletter</h2>
    <p>Get lifetime access for ONLY $97 before it becomes a monthly Subscription</p>
    <div class="nl-form"><div class="field">Enter Your Name</div><div class="field">Enter Your Email</div><div class="submit">SUBSCRIBE NOW</div></div>
  </div>
</section>

<section class="authors">
  <div class="wrap">
    <h2>ABOUT OUR AUTHORS</h2>
    <div class="dots"><i></i><i></i><i></i></div>
    <div class="author-grid">
      <div class="author"><div class="ph" role="img" aria-label="Portrait photo of author Daniel Harper" style="background:linear-gradient(135deg,#c8c8c8,#8a7a70)"></div><div><h3>Daniel Harper</h3><small>Author</small><p>Lorem Ipsum is simply dummy text of the printing and typesetting industry. Lorem Ipsum has been the industry's standard dummy text ever since the 1500s, when an unknown printer took a galley of type.</p><div class="socials"><i></i><i></i><i></i></div><span class="btn-outline">Read More ›</span></div></div>
      <div class="author"><div class="ph" role="img" aria-label="Portrait photo of author Nadia Quinn" style="background:linear-gradient(135deg,#d8d0c8,#7a5a4a)"></div><div><h3>Nadia Quinn</h3><small>Author</small><p>Lorem Ipsum is simply dummy text of the printing and typesetting industry. Lorem Ipsum has been the industry's standard dummy text ever since the 1500s, when an unknown printer took a galley of type.</p><div class="socials"><i></i><i></i><i></i></div><span class="btn-outline">Read More ›</span></div></div>
    </div>
  </div>
</section>

<section class="testimonials">
  <h2>Testimonials</h2>
  <div class="avatar" role="img" aria-label="Portrait of reviewer Evan Marsh"></div>
  <blockquote>“ Lorem Ipsum is simply dummy text of the printing and typesetting industry. Lorem Ipsum has been the industry's standard dummy text ever since the 1500s, when an unknown printer took a galley of type and scrambled it to make a type specimen book. It has survived not only five centuries, but also the leap into electronic typesetting, remaining essentially unchanged. ”</blockquote>
  <div class="who">Evan Marsh</div>
  <div class="arrow l"><svg width="10" height="10" viewBox="0 0 10 10"><path d="M7 1 L3 5 L7 9" fill="none" stroke="#555" stroke-width="1.5"/></svg></div>
  <div class="arrow r"><svg width="10" height="10" viewBox="0 0 10 10"><path d="M3 1 L7 5 L3 9" fill="none" stroke="#555" stroke-width="1.5"/></svg></div>
</section>

<section class="guarantee">
  <div class="badge" role="img" aria-label="Thirty day money-back guarantee badge"></div>
  <h3>Ready to Start Selling More Books?</h3>
  <h2>Risk-Free!</h2>
  <p>30 Day Money-Back Guarantee</p>
  <span class="cta">Get It Now!</span>
</section>

<footer class="site-footer">
  <div class="wrap foot-grid">
    <div>
      <h4>Contact Info</h4>
      <div class="contact-item"><svg width="12" height="14" viewBox="0 0 12 14"><path d="M6 0a5 5 0 0 1 5 5c0 4-5 9-5 9S1 9 1 5a5 5 0 0 1 5-5z" fill="#fff"/><circle cx="6" cy="5" r="2" fill="#2b2b2b"/></svg><div><b>Address:</b>Lindenweg 8, Meerdorp,<br>Nederland</div></div>
      <div class="contact-item"><svg width="12" height="12" viewBox="0 0 12 12"><path d="M2 0l3 3-1.5 1.5a7 7 0 0 0 4 4L9 7l3 3-2 2C5 12 0 7 0 2z" fill="#fff"/></svg><div><b>Telephone:</b>1800-555-0142 EXT: 001</div></div>
      <div class="contact-item"><svg width="12" height="10" viewBox="0 0 12 10"><rect width="12" height="10" fill="#fff"/><path d="M0 0 L6 5 L12 0" fill="none" stroke="#2b2b2b"/></svg><div><b>Email:</b>info@northlinepress.com</div></div>
      <div class="contact-item"><svg width="12" height="12" viewBox="0 0 12 12"><circle cx="6" cy="6" r="5.5" fill="none" stroke="#fff"/><path d="M0.5 6h11M6 0.5v11" stroke="#fff"/></svg><div><b>Website:</b>www.northlinepress.com</div></div>
    </div>
    <div>
      <h4>Instagram Feeds</h4>
      <div class="insta" role="img" aria-label="Grid of sixteen recent social photo thumbnails">
        <i style="background:#8a5a6a"></i><i style="background:#4a6a9a"></i><i style="background:#a07a5a"></i><i style="background:#6a3a5a"></i>
        <i style="background:#5a5a7a"></i><i style="background:#9a6a4a"></i><i style="background:#3a4a6a"></i><i style="background:#7a4a7a"></i>
        <i style="background:#a08070"></i><i style="background:#4a3a5a"></i><i style="background:#8a6a8a"></i><i style="background:#5a6a8a"></i>
        <i style="background:#6a4a4a"></i><i style="background:#9a7a8a"></i><i style="background:#4a5a4a"></i><i style="background:#7a6a5a"></i>
      </div>
    </div>
    <div>
      <h4>Apply Now</h4>
      <div class="ff">Enter your name</div>
      <div class="ff">Enter your email</div>
      <div class="ff msg">Enter your message</div>
      <span class="send">Submit</span>
    </div>
  </div>
</footer>

<div class="bottom-bar">
  <nav>Home · About NLP · Apply Now · NLP Worlds · NLP Authors · FAQ · News · Contact</nav>
  <small>© 2018 Northline Press, LLC. All rights reserved.</small>
</div>

</body>
</html>
```